Retail Jewelry Business Card Design Project

We are in need of a new business card design for a retail jewelry store. This store is in the business of fine jewelry including but not specific to bridal jewelry, diamonds, designer jewelry and watches.

This store has been in business for 20 years but continues to strive for a modern professional appeal. The main colors use for this business are a royal blue, white and silver.

Target Market(s)

Target market is ages 18-50

Industry/Entity Type

Jewelry

Requirements
Must have
• Sales Person Name
Sales Person Email Address

Store Address
Store Phone
Website

Standard business card size. No odd shapes or sizes.
Nice to have
• Overall modern feel for card.

We have thought that a design with a nice feature of the logo on the back of the card would be nice but open to ideas.
Should not have
• No specific images of jewelry should be used.

```html
<!DOCTYPE html>
<html lang="en">
<head>
<meta charset="utf-8">
<title>Harlan Reed Fine Jewelry – Business Cards</title>
<link rel="stylesheet" href="https://fonts.googleapis.com/css2?family=Tinos:ital,wght@0,400;0,700;1,700&family=Arimo:wght@400&display=swap">
<style>
  :root {
    --royal-blue: #2b2f93;
    --band-light: #6a6cc0;
    --band-pale: #c9caea;
    --rule: #7a7cc6;
    --ink: #3a3a3a;
    --card: #ffffff;
    --backdrop: #e9e9ec;
    --edge: #d2d2d8;
  }
  * { box-sizing: border-box; margin: 0; padding: 0; }
  html, body {
    width: 1200px; height: 804px; overflow: hidden;
    background: var(--backdrop);
  }
  .stage {
    position: relative; width: 1200px; height: 804px;
    display: flex; align-items: center; justify-content: center; gap: 40px;
  }
  .card {
    position: relative; width: 520px; height: 297px;
    background: var(--card);
    border: 1px solid var(--edge);
    box-shadow: 0 6px 18px rgba(0,0,0,0.12);
    overflow: hidden;
  }

  .brand-name {
    font-family: "Tinos", serif; font-weight: 700;
    color: var(--royal-blue); line-height: 1.05; text-align: center;
  }
  .brand-name .brand-main { display: block; }
  .brand-name .brand-rule { display: block; height: 2px; background: var(--rule); }
  .brand-name .brand-sub { display: block; }

  /* Front: contact side */
  .card-front .wave { position: absolute; inset: 0; width: 100%; height: 100%; }
  .card-front .brand-name { position: absolute; left: 100px; top: 16px; width: 240px; }
  .card-front .brand-main { font-size: 36px; }
  .card-front .brand-rule { margin: 3px 0 4px; }
  .card-front .brand-sub { font-size: 18px; letter-spacing: 3px; }

  .store-address {
    position: absolute; left: 108px; top: 128px;
    font-family: "Tinos", serif; font-style: normal;
    font-size: 13px; color: var(--ink); line-height: 1.6;
  }
  .divider {
    position: absolute; left: 264px; top: 100px; width: 1px; height: 66px;
    background: #bdbdc6;
  }
  .contact-list {
    position: absolute; left: 276px; top: 100px; list-style: none;
    font-family: "Tinos", serif; font-size: 13px; color: var(--ink);
  }
  .contact-list li { display: flex; align-items: center; gap: 7px; height: 22px; }
  .contact-list svg { width: 11px; height: 11px; flex: none; }
  .sales-name {
    position: absolute; left: 58px; bottom: 12px;
    font-family: "Tinos", serif; font-weight: 700; font-style: italic;
    font-size: 15px; color: #ffffff; letter-spacing: 0.5px; white-space: nowrap;
    transform: rotate(-5deg); transform-origin: left bottom;
  }

  /* Back: brand side */
  .card-back { display: flex; flex-direction: column; align-items: center; justify-content: center; }
  .card-back .brand-name { width: 330px; }
  .card-back .brand-main { font-size: 52px; }
  .card-back .brand-rule { margin: 4px 0 6px; }
  .card-back .brand-sub { font-size: 27px; letter-spacing: 4px; }
  .website {
    margin-top: 34px;
    font-family: "Arimo", sans-serif; font-size: 15px; letter-spacing: 2px; color: var(--ink);
  }
</style>
</head>
<body>
<main class="stage">
  <section class="card card-front" aria-label="Business card, contact side">
    <svg class="wave" viewBox="0 0 520 297" preserveAspectRatio="none" aria-hidden="true">
      <path d="M0 297 L0 240 C170 238 340 225 520 172 L520 297 Z" fill="var(--band-pale)"/>
      <path d="M0 297 L0 247 C170 245 342 232 520 180 L520 297 Z" fill="var(--band-light)"/>
      <path d="M0 297 L0 255 C170 253 344 240 520 189 L520 297 Z" fill="#ffffff"/>
      <path d="M0 297 L0 260 C170 258 346 246 520 195 L520 297 Z" fill="var(--royal-blue)"/>
    </svg>
    <h1 class="brand-name">
      <span class="brand-main">Harlan Reed</span>
      <span class="brand-rule"></span>
      <span class="brand-sub">FINE JEWELRY</span>
    </h1>
    <address class="store-address">2280 Linden Avenue<br>Bay Harbor, FL 32409</address>
    <div class="divider"></div>
    <ul class="contact-list">
      <li>
        <svg viewBox="0 0 12 12" aria-hidden="true"><circle cx="6" cy="6" r="5.5" fill="none" stroke="var(--ink)"/><path d="M4 3.2 L5 4.6 L4.5 5.3 Q5.4 6.8 6.7 7.5 L7.4 7 L8.8 8 L8.2 8.9 Q5.5 8.8 3.2 4 Z" fill="var(--ink)"/></svg>
        555-218-4470
      </li>
      <li>
        <svg viewBox="0 0 12 12" aria-hidden="true"><rect x="1" y="2.5" width="10" height="7" fill="var(--ink)"/><path d="M1 2.5 L6 6.5 L11 2.5" fill="none" stroke="#fff" stroke-width="1"/></svg>
        harlan@harlanreedjewelry.com
      </li>
      <li>
        <svg viewBox="0 0 12 12" aria-hidden="true"><circle cx="6" cy="6" r="5.5" fill="var(--ink)"/><path d="M0.8 6 H11.2 M6 0.8 V11.2 M6 0.8 Q2.5 6 6 11.2 M6 0.8 Q9.5 6 6 11.2" fill="none" stroke="#fff" stroke-width="0.7"/></svg>
        www.harlanreedjewelry.com
      </li>
    </ul>
    <p class="sales-name">Harlan Reed Whitmore</p>
  </section>

  <section class="card card-back" aria-label="Business card, brand side">
    <h2 class="brand-name">
      <span class="brand-main">Harlan Reed</span>
      <span class="brand-rule"></span>
      <span class="brand-sub">FINE JEWELRY</span>
    </h2>
    <p class="website">www.harlanreedjewelry.com</p>
  </section>
</main>
</body>
</html>
```